Quenda-Ro Flyer (Business Launch)

Using my existing log design for Quenda-Ro Mobile Mechanics, I would like a flyer designed. This would be used for advertising, letterbox drops, handing to the public , door knocking ect.

I'm looking for clean cut simple though with the wow factor, I was thinking of even having the flyer in the shape of a van to promote that I'm a mobile business (I come to you ect)

I've attached copies of my logo and business cards.

I would like the following list of services we provide listed on the flyer (see back of business card).
7 day service (we come to you)
10% discount for online/email booking-enquiry

I think this should be enough for now.

I'm launching this business to aiming to hit the ground running,

Target Market(s)

All motor vehicle owners, house holds, businesses

Industry/Entity Type

Automotive

Font styles to use
Sans Serif
Other font styles liked:
• refer images

Colors
0355a3

Requirements
Must have
• services offered, logo, 7 days, we come to or or catchy phrase to let people know this.
• 10% discount for online/email booking enquiries
• Maintenance Package Servicing from $149 conditions apply
• my preference is for blue, grey and while colour scheme, though also happy to accept artistic design ideas to these.
Nice to have
• Wow factor, brochure that stand out from the rest
• Different share brochure in shape of work van (refer velkaro tramix van)
Should not have
• Not looking for a cheap quick fix, I'm wanting to create a brand .

```html
<!DOCTYPE html>
<html lang="en">
<head>
<meta charset="utf-8">
<title>Quenda-Ro Mobile Mechanics – Flyer</title>
<link href="https://fonts.googleapis.com/css2?family=Bebas+Neue&family=Oswald:wght@500;600;700&family=Roboto+Condensed:wght@400&display=swap" rel="stylesheet">
<style>
  :root {
    --brand-blue: #1f8ffa;
    --ink: #2b2d30;
    --contact-ink: #111111;
    --white: #ffffff;
    --backdrop: #33251e;
  }
  html, body {
    margin: 0;
    width: 1200px;
    height: 738px;
    overflow: hidden;
    background: var(--backdrop);
  }
  .flyer {
    position: absolute;
    left: 355px;
    top: 21px;
    width: 490px;
    height: 695px;
    background: var(--brand-blue);
    color: var(--white);
    font-family: "Bebas Neue", "Oswald", sans-serif;
    overflow: hidden;
  }
  .header {
    position: absolute;
    inset: 0 0 auto 0;
    height: 130px;
    background: var(--white);
  }
  .brand-dot {
    position: absolute;
    left: 58px;
    top: 18px;
    width: 90px;
    height: 90px;
    border-radius: 50%;
    background: var(--brand-blue);
  }
  .brand-name {
    position: absolute;
    left: 172px;
    top: 22px;
    margin: 0;
    color: var(--ink);
    font-family: "Oswald", sans-serif;
    font-weight: 600;
    line-height: 1;
  }
  .brand-name .primary { display: block; font-size: 54px; letter-spacing: 0.5px; }
  .brand-name .secondary { display: block; font-size: 22px; letter-spacing: 1.6px; margin-top: 4px; }
  .services-band {
    position: absolute;
    left: 0; right: 0;
    top: 130px;
    height: 50px;
    border-bottom: 10px solid var(--white);
    text-align: center;
    font-size: 40px;
    line-height: 52px;
    letter-spacing: 0.5px;
  }
  .line {
    position: absolute;
    left: 0; right: 0;
    margin: 0;
    text-align: center;
    line-height: 1;
    white-space: nowrap;
  }
  .headline { font-size: 78px; top: 190px; }
  .days { font-family: "Oswald", sans-serif; font-weight: 600; font-size: 38px; letter-spacing: 2.6px; top: 264px; }
  .discount { font-size: 60px; top: 310px; }
  .discount .figure { font-family: "Oswald", sans-serif; font-weight: 700; font-size: 52px; }
  .enquiries { font-size: 32px; letter-spacing: 2px; top: 366px; }
  .package { font-size: 62px; top: 404px; line-height: 50px; }
  .price { font-size: 32px; letter-spacing: 2px; top: 510px; }
  .price .amount { font-family: "Oswald", sans-serif; font-weight: 700; font-size: 40px; letter-spacing: 0; }
  .chevron { position: absolute; inset: 0; }
  .contact {
    position: absolute;
    font-family: "Roboto Condensed", sans-serif;
    color: var(--contact-ink);
    line-height: 30px;
    list-style: none;
    margin: 0;
    padding: 0;
  }
  .contact li { display: flex; align-items: center; gap: 5px; white-space: nowrap; }
  .contact svg { flex: none; }
  .contact.phones { left: 36px; top: 618px; font-size: 25px; }
  .contact.online { left: 232px; right: 10px; top: 620px; font-size: 21px; letter-spacing: -0.2px; }
</style>
</head>
<body>
<main class="flyer">
  <header class="header">
    <span class="brand-dot" aria-hidden="true"></span>
    <h1 class="brand-name"><span class="primary">Quenda-Ro</span><span class="secondary">MOBILE MECHANICS</span></h1>
  </header>

  <div class="services-band">SERVICES OFFERED</div>

  <p class="line headline">MOBILE SERVICE</p>
  <p class="line days">7 DAYS A WEEK</p>
  <p class="line discount"><span class="figure">10%</span> DISCOUNT</p>
  <p class="line enquiries">ONLINE / EMAIL BOOKING ENQUIRIES</p>
  <p class="line package">MAINTENANCE<br>PACKAGE SERVICING</p>
  <p class="line price">FROM <span class="amount">$149</span> CONDITIONS APPLY</p>

  <svg class="chevron" viewBox="0 0 490 695" aria-hidden="true">
    <polygon points="0,540 245,594 490,528 490,548 245,610 0,561" fill="#ffffff"/>
  </svg>

  <ul class="contact phones">
    <li>
      <svg width="19" height="19" viewBox="0 0 24 24"><path fill="#111" d="M6.6 10.8a15.1 15.1 0 0 0 6.6 6.6l2.2-2.2a1 1 0 0 1 1-.25 11.4 11.4 0 0 0 3.6.57 1 1 0 0 1 1 1V20a1 1 0 0 1-1 1A17 17 0 0 1 3 4a1 1 0 0 1 1-1h3.5a1 1 0 0 1 1 1c0 1.25.2 2.45.57 3.57a1 1 0 0 1-.25 1z"/></svg>
      1300 555 018
    </li>
    <li>
      <svg width="19" height="25" viewBox="0 0 16 26"><rect x="2" y="1" width="12" height="24" rx="2" fill="none" stroke="#111" stroke-width="2"/><rect x="6" y="21" width="4" height="1.6" fill="#111"/></svg>
      0400 555 782
    </li>
  </ul>

  <ul class="contact online">
    <li>
      <svg width="20" height="20" viewBox="0 0 24 24"><circle cx="12" cy="12" r="11" fill="#111"/><path d="M6 8h12v8H6z" fill="none" stroke="#fff" stroke-width="1.4"/><path d="M6 8l6 5 6-5" fill="none" stroke="#fff" stroke-width="1.4"/></svg>
      admin@quenda-ro.com.au
    </li>
    <li>
      <svg width="20" height="20" viewBox="0 0 24 24" fill="none" stroke="#111" stroke-width="1.6"><circle cx="12" cy="12" r="10"/><ellipse cx="12" cy="12" rx="4.5" ry="10"/><path d="M2 12h20M4 7h16M4 17h16"/></svg>
      www.quenda-ro.com.au
    </li>
  </ul>
</main>
</body>
</html>
```